Fundvaulter project image

I need a image created that will be the forward face of our Fundvaulter campaign. Our project is a Linkwave programmable led dog collar controlled by a smart phone app that allows you to individually control the LED's on the collar. It includes solid color, strobe, and fade effects. The resolution needs to be at least 640x by 480x and be 4:3 aspect ratio as this what is required by Fundvaulter. I uploaded a few pictures of the prototypes and app. These do not have to be included in the image you create and are just to give you an idea of the product. The rest I leave to you, use your imagination and go nuts :) Thanks.

```html
<!DOCTYPE html>
<html lang="en">
<head>
<meta charset="utf-8">
<title>LED Dog Collar – Fundvaulter Campaign</title>
<link rel="stylesheet" href="https://fonts.googleapis.com/css2?family=Josefin+Sans:wght@300;400&display=swap">
<style>
  :root {
    --sky-top: #2f6fae;
    --sky-mid: #6f9fcc;
    --sky-low: #c4d7e6;
    --horizon: #9aa7b4;
    --treeline: #2b3038;
    --dog-dark: #2a2e35;
    --dog-mid: #6b717b;
    --dog-light: #dfe3e8;
    --band: rgba(20, 40, 70, 0.28);
    --tile-fill: rgba(30, 40, 55, 0.45);
    --text: #ffffff;
    --text-soft: rgba(255, 255, 255, 0.94);
  }
  * { margin: 0; padding: 0; box-sizing: border-box; }
  html, body { width: 1200px; height: 900px; overflow: hidden; }
  body { font-family: "Josefin Sans", "Helvetica Neue", sans-serif; color: var(--text); }

  .campaign-card { position: relative; width: 1200px; height: 900px; overflow: hidden; }

  .hero-backdrop {
    position: absolute; inset: 0;
    background: linear-gradient(180deg,
      var(--sky-top) 0%, var(--sky-mid) 35%, var(--sky-low) 62%,
      var(--horizon) 74%, var(--treeline) 88%, #1d2128 100%);
  }

  .hero-subject {
    position: absolute; left: 85px; top: 10px; width: 495px; height: 890px;
    border-radius: 46% 46% 6% 6% / 30% 30% 4% 4%;
    background: linear-gradient(180deg,
      var(--dog-dark) 0%, var(--dog-mid) 30%, var(--dog-light) 55%, var(--dog-mid) 100%);
    opacity: 0.9;
  }

  .text-band {
    position: absolute; left: 544px; top: 318px; width: 656px; height: 323px;
    background: var(--band);
  }

  .headline {
    position: absolute; left: 571px; top: 336px;
    font-weight: 300; font-size: 46px; letter-spacing: 3.4px; white-space: nowrap;
    text-shadow: 0 1px 3px rgba(0,0,0,0.3);
  }

  .description {
    position: absolute; left: 571px; top: 425px; width: 620px;
    font-weight: 300; font-size: 26px; line-height: 34px; letter-spacing: 1.4px;
    white-space: nowrap; color: var(--text-soft);
    text-shadow: 0 1px 2px rgba(0,0,0,0.3);
  }
  .description p + p { margin-top: 32px; }

  .feature-list { position: absolute; top: 666px; left: 0; width: 1200px; list-style: none; }
  .feature { position: absolute; width: 131px; text-align: center; }
  .feature--led { left: 600px; }
  .feature--phone { left: 789px; }
  .feature--wireless { left: 979px; }

  .feature-tile {
    width: 131px; height: 128px; border: 4px solid var(--text);
    border-radius: 22px; background: var(--tile-fill);
    display: flex; align-items: center; justify-content: center;
  }
  .feature-label {
    display: block; margin-top: 24px; margin-left: -40px; width: 211px;
    font-weight: 300; font-size: 24px; line-height: 33px; letter-spacing: 1.5px;
  }
</style>
</head>
<body>
<main class="campaign-card">
  <div class="hero-backdrop" role="img" aria-label="Blue cloudy sky above a snowy winter treeline"></div>
  <div class="hero-subject" role="img" aria-label="Photo of a black and white husky standing and facing forward, wearing a glowing blue LED collar"></div>

  <div class="text-band"></div>

  <h1 class="headline">LED DOG COLLAR</h1>

  <div class="description">
    <p>Linkwave programmable led dog collar<br>controlled by a smart phone app.</p>
    <p>individuall LED control on the collar.<br>It includes solid color, strobe, and fade<br>effects.</p>
  </div>

  <ul class="feature-list">
    <li class="feature feature--led">
      <div class="feature-tile">
        <svg width="64" height="96" viewBox="0 0 64 96" aria-hidden="true">
          <path d="M6 34 A26 26 0 0 1 58 34 V64 H6 Z" fill="#fff"/>
          <rect x="2" y="64" width="60" height="6" fill="#fff"/>
          <rect x="18" y="70" width="4" height="24" fill="#fff"/>
          <rect x="42" y="70" width="4" height="18" fill="#fff"/>
        </svg>
      </div>
      <span class="feature-label">LED</span>
    </li>
    <li class="feature feature--phone">
      <div class="feature-tile">
        <svg width="50" height="96" viewBox="0 0 50 96" aria-hidden="true">
          <rect x="2" y="2" width="46" height="92" rx="8" fill="#fff"/>
          <rect x="9" y="12" width="32" height="30" fill="#333"/>
          <g fill="#333">
            <rect x="10" y="52" width="8" height="6"/><rect x="21" y="52" width="8" height="6"/><rect x="32" y="52" width="8" height="6"/>
            <rect x="10" y="62" width="8" height="6"/><rect x="21" y="62" width="8" height="6"/><rect x="32" y="62" width="8" height="6"/>
            <rect x="10" y="72" width="8" height="6"/><rect x="21" y="72" width="8" height="6"/><rect x="32" y="72" width="8" height="6"/>
            <rect x="10" y="82" width="8" height="5"/><rect x="21" y="82" width="8" height="5"/><rect x="32" y="82" width="8" height="5"/>
          </g>
        </svg>
      </div>
      <span class="feature-label">Smart phone controll</span>
    </li>
    <li class="feature feature--wireless">
      <div class="feature-tile">
        <svg width="40" height="40" viewBox="0 0 40 40" aria-hidden="true">
          <circle cx="20" cy="20" r="17" fill="#fff"/>
        </svg>
      </div>
      <span class="feature-label">Linkwave</span>
    </li>
  </ul>
</main>
</body>
</html>
```